Journal of a NOVICE
Book One in the Series
Chronicles of a Seer
* * *
There are four books in the series
Book 1 - Journal of a Novice
Book 2 - Journal of a Wayfarer
Book 3 - Journal of a NightHeron
Book 4 - The Ancient Logs
You can read stories from the first book here - www.seerjournal.com
* * *
I am looking for a cover for the first book. For consistency, I would like to see whatever themes or concepts are used on this book’s cover, that similar themes/concepts are used throughout the series.
* * *
Themes
The only theme I am sure about is having a colour for each book. The first book is Green – that is, the predominant colour is to be green, rather than simply a green cover. There may be other ideas or themes associated with it, or different colours used, etc …
I imagine the four books lined up on a bookshelf. The colour is to help differentiate the books, to make each more visibly accessible.
* * *
Spine
Going with the colour theme for each book, I wonder if the font on the spine is to be in green, or the background is to be green. I guess this depends on the design of the cover itself … But, once again, the idea being that consistency is used throughout the series.
* * *
Symbolism
The book has been written with the idea that these stories could have happened anywhere, anytime, to anyone. With this in mind, I want to avoid using any kind of Australiana or Aboriginal symbolism.
* * *
Thanks,
Gareth.

```html
<!DOCTYPE html>
<html lang="en">
<head>
<meta charset="utf-8">
<title>Journal of a Novice — Cover Wrap</title>
<link rel="stylesheet" href="https://fonts.googleapis.com/css2?family=Inter:wght@200;300;800;900&display=swap">
<style>
  :root {
    --paper: #f7f7f7;
    --paper-edge: #d9dbd8;
    --ghost-type: #e4e5e8;
    --ghost-type-thin: #e6e7ea;
    --rule-blue: #1b8fd8;
    --leaf-green: #b0dd26;
    --ink: #3b3f49;
    --ink-light: #5d6270;
    --spine-type: #ffffff;
    --fold-line: #333333;
  }
  html, body {
    margin: 0;
    padding: 0;
    overflow: hidden;
    background: #ffffff;
  }
  .cover-wrap {
    position: relative;
    width: 1200px;
    height: 667px;
    overflow: hidden;
    background: var(--paper);
    font-family: "Inter", "Helvetica Neue", Arial, sans-serif;
  }
  .ghost-title {
    position: absolute;
    left: 0;
    top: 0;
    margin: 0;
    white-space: nowrap;
    line-height: 1;
  }
  .ghost-title__lead {
    position: absolute;
    left: 10px;
    top: -14px;
    font-weight: 200;
    font-size: 188px;
    letter-spacing: -4px;
    color: var(--ghost-type-thin);
  }
  .ghost-title__main {
    position: absolute;
    left: 18px;
    top: 148px;
    font-weight: 900;
    font-size: 196px;
    letter-spacing: 2px;
    color: var(--ghost-type);
  }
  .rule-band {
    position: absolute;
    left: 0;
    top: 300px;
    width: 1200px;
    height: 16px;
    background: var(--rule-blue);
  }
  .colour-field {
    position: absolute;
    left: 0;
    top: 316px;
    width: 1200px;
    height: 351px;
    background: var(--leaf-green);
  }
  .spine {
    position: absolute;
    left: 567px;
    top: 0;
    width: 67px;
    height: 667px;
  }
  .spine__rule {
    position: absolute;
    left: 0;
    top: 146px;
    width: 67px;
    height: 16px;
    background: var(--rule-blue);
  }
  .spine__field {
    position: absolute;
    left: 0;
    top: 162px;
    width: 67px;
    height: 505px;
    background: var(--leaf-green);
  }
  .spine__series {
    position: absolute;
    left: 34px;
    top: 72px;
    transform: translate(-50%, -50%) rotate(90deg);
    font-weight: 300;
    font-size: 20px;
    color: var(--ink);
    white-space: nowrap;
  }
  .spine__title {
    position: absolute;
    left: 33px;
    top: 185px;
    transform-origin: 0 0;
    transform: rotate(90deg) translateY(-50%);
    white-space: nowrap;
    color: var(--spine-type);
    font-size: 27px;
    line-height: 1;
  }
  .spine__title-lead { font-weight: 200; }
  .spine__title-main { font-weight: 900; letter-spacing: 1px; margin-left: 6px; }
  .fold-line {
    position: absolute;
    top: 0;
    width: 0;
    height: 667px;
    border-left: 1px dashed var(--fold-line);
  }
  .fold-line--back { left: 567px; }
  .fold-line--front { left: 634px; }
  .front-title {
    position: absolute;
    left: 666px;
    top: 172px;
    margin: 0;
    line-height: 1;
  }
  .front-title__lead {
    display: block;
    font-weight: 200;
    font-size: 62px;
    letter-spacing: -1.5px;
    color: var(--ink-light);
  }
  .front-title__main {
    display: block;
    margin-top: 6px;
    font-weight: 900;
    font-size: 56px;
    letter-spacing: 1px;
    color: var(--ink);
  }
  .vignette {
    position: absolute;
    inset: 0;
    pointer-events: none;
    background:
      radial-gradient(ellipse 75% 80% at 50% 48%, rgba(0,0,0,0) 60%, rgba(40,50,30,0.22) 100%);
  }
</style>
</head>
<body>
  <main class="cover-wrap">
    <div class="ghost-title" aria-hidden="true">
      <span class="ghost-title__lead">Journal of a</span>
      <span class="ghost-title__main">NOVICE</span>
    </div>

    <div class="rule-band"></div>
    <div class="colour-field"></div>

    <section class="spine" aria-label="Spine">
      <div class="spine__series">Chronicles</div>
      <div class="spine__rule"></div>
      <div class="spine__field"></div>
      <div class="spine__title">
        <span class="spine__title-lead">Journal of a</span><span class="spine__title-main">NOVICE</span>
      </div>
    </section>

    <div class="fold-line fold-line--back"></div>
    <div class="fold-line fold-line--front"></div>

    <h1 class="front-title">
      <span class="front-title__lead">Journal of a</span>
      <span class="front-title__main">NOVICE</span>
    </h1>

    <div class="vignette"></div>
  </main>
</body>
</html>
```